I need a website design for a unique tropical home in the Whitsundays. It is called the Kerrow Vale and would like an African Baobab tree as a logo. It is an eco retreat on the ocean/beach with a large award winning house. Is suited to special celebrations, boutique weddings, Executive retreats. Have many wonderful photographs to be added. Should allow for contact to arrange a booking and if possible have a pricing and bookings calendar. Can look at Pelvanto.com.au as example.
Home page should have picture of house from air and description of the special uses as mentioned above. Can then go to next level for descriptions of rooms, features, attractions, rates, booking calendar and contact details.

```html
<!DOCTYPE html>
<html lang="en">
<head>
<meta charset="utf-8">
<title>Kerrow Vale</title>
<link rel="stylesheet" href="https://fonts.googleapis.com/css2?family=Arimo:wght@400;700&display=swap">
<style>
:root{
  --brown:#a65a0f;
  --brown-dark:#8a4706;
  --brown-light:#c57a26;
  --orange:#f0a232;
  --text:#222;
  --panel:#efefef;
  --social:#bdbdbd;
  --logo-green:#2f9a3a;
  --cal-blue:#2b7bb9;
}
*{box-sizing:border-box;margin:0;padding:0}
html,body{width:916px;height:1200px;overflow:hidden;background:#fff}
body{position:relative;font-family:"Arimo",Arial,sans-serif;color:var(--text)}
.abs{position:absolute}

.logo-mark{left:51px;top:26px;width:95px;height:118px;background:var(--logo-green);border:3px solid #1d6d25}
.site-name{left:154px;top:45px;font-size:21px;font-weight:700;color:var(--brown)}
.social{top:38px;display:flex;gap:13px;left:729px}
.social span{width:24px;height:24px;border-radius:50%;background:var(--social);display:block}

.hero{left:24px;top:75px;width:876px;height:354px;border:2px solid #cfcfcf;overflow:hidden;
  background:linear-gradient(#c9cfd2 0%,#8d9599 25%,#5d5f58 32%,#8a7552 45%,#9c7c4c 70%,#6f5634 100%)}
.hero-arrow{width:60px;height:60px;border-radius:50%;background:rgba(150,150,150,.85);display:flex;align-items:center;justify-content:center}
.hero-arrow.prev{left:17px;top:156px}
.hero-arrow.next{left:796px;top:164px}

.nav{left:24px;top:433px;width:874px;height:34px;background:linear-gradient(var(--brown-light),var(--brown) 55%,var(--brown-dark))}
.nav a{position:absolute;top:8px;color:#fff;font-weight:700;font-size:15px;text-decoration:none}

.side-head{left:24px;width:207px;height:26px;background:linear-gradient(var(--brown-light),var(--brown));color:#fff;font-weight:700;font-size:15px;text-align:center;line-height:26px}
.side-head::after{content:"";position:absolute;left:50%;bottom:-7px;margin-left:-8px;border:8px solid transparent;border-bottom:0;border-top-color:var(--brown)}
.side-head.light{font-weight:400}

.date-label{left:25px;top:530px;font-size:10px}
.date-input{left:55px;top:525px;width:134px;height:18px;border:1px solid #777;font-size:10px;padding:2px 4px}

.calendar{left:55px;top:546px;width:177px;height:183px;border:1px solid #ccc;background:#f7f7f7;padding:2px;font-size:9px}
.cal-head{height:22px;background:linear-gradient(#f6b64a,var(--orange));border-radius:3px;color:#fff;display:flex;align-items:center;justify-content:space-between;padding:0 4px}
.cal-head i{width:11px;height:11px;border-radius:50%;background:#fff;display:block}
.cal-grid{width:100%;border-collapse:separate;border-spacing:3px;margin-top:4px}
.cal-grid th{font-weight:400;color:#333;height:14px}
.cal-grid td{height:17px;border:1px solid #ccd;background:#fff;color:var(--cal-blue);text-align:right;padding-right:2px}
.cal-grid td.today{background:#fbe98a;border-color:#e0c040;color:#333}
.cal-btn{top:153px;height:22px;border:1px solid #bbb;border-radius:3px;background:#fff;color:#8aa;font-size:10px;line-height:20px;text-align:center}

.service-photo{left:24px;top:781px;width:207px;height:154px;background:linear-gradient(90deg,#c8d4dc,#e9edf0 45%,#dcd2c8)}
.news{left:26px;top:986px;width:214px;font-size:11px;line-height:13.5px}

.btn{height:21px;border-radius:4px;background:linear-gradient(var(--brown-light),var(--brown));color:#fff;font-size:13px;text-align:center;line-height:21px}

.main{left:249px;top:483px;width:649px;height:587px;border:2px solid #d6d6d6}
.card{top:17px;width:206px;height:323px;background:var(--panel)}
.card .photo{position:absolute;left:5px;top:5px;width:195px;height:140px}
.card h3{position:absolute;left:15px;top:155px;font-size:15.5px;color:#333}
.card p{position:absolute;left:0;top:176px;width:214px;font-size:11px;line-height:13.5px;letter-spacing:-.1px}
.card .btn{position:absolute;top:295px;width:80px}
.main h2{position:absolute;left:11px;top:371px;font-size:17px;color:var(--brown);font-weight:700}
.main hr{position:absolute;left:11px;top:395px;width:627px;border:0;border-top:2px solid var(--brown)}
.main .body{position:absolute;left:18px;top:406px;width:625px;font-size:11px;line-height:13.4px}

.rule-thick{left:9px;top:1130px;width:890px;height:4px;background:var(--brown)}
.rule-thin{left:9px;top:1137px;width:890px;height:1px;background:var(--brown)}
.footer-name{left:9px;top:1148px;font-size:15.5px;color:var(--brown)}
.footer-line{left:9px;font-size:12.5px;line-height:14px;color:var(--brown)}
.copyright{left:776px;top:1150px;font-size:14.5px;color:var(--brown)}
</style>
</head>
<body>

<header>
  <div class="abs logo-mark"></div>
  <div class="abs site-name">Kerrow Vale</div>
  <div class="abs social"><span></span><span></span><span></span><span></span><span></span></div>
</header>

<div class="abs hero" role="img" aria-label="Couple walking along a sandy beach towards the sea at dusk">
  <div class="abs hero-arrow prev"><svg width="26" height="26" viewBox="0 0 26 26"><path d="M20 4 L6 13 L20 22" fill="none" stroke="#fff" stroke-width="4"/></svg></div>
  <div class="abs hero-arrow next"><svg width="26" height="26" viewBox="0 0 26 26"><path d="M6 4 L20 13 L6 22" fill="none" stroke="#fff" stroke-width="4"/></svg></div>
</div>

<nav class="abs nav">
  <a style="left:24px">Home</a>
  <a style="left:94px">Rooms</a>
  <a style="left:165px">Features</a>
  <a style="left:255px">Attractions</a>
  <a style="left:363px">Rates</a>
  <a style="left:428px">Booking</a>
  <a style="left:520px">Contact</a>
</nav>

<aside>
  <div class="abs side-head" style="top:485px">Check Rooms</div>
  <div class="abs date-label">Date:</div>
  <div class="abs date-input">25 February 2009 3.40pm</div>
  <div class="abs calendar">
    <div class="cal-head"><i></i><span>February 2009</span><i></i></div>
    <table class="cal-grid">
      <tr><th>Su</th><th>Mo</th><th>Tu</th><th>We</th><th>Th</th><th>Fr</th><th>Sa</th></tr>
      <tr><td>1</td><td>2</td><td>3</td><td>4</td><td>5</td><td>6</td><td>7</td></tr>
      <tr><td>8</td><td>9</td><td>10</td><td>11</td><td>12</td><td>13</td><td>14</td></tr>
      <tr><td>15</td><td>16</td><td>17</td><td>18</td><td>19</td><td>20</td><td>21</td></tr>
      <tr><td>22</td><td>23</td><td>24</td><td class="today">25</td><td>26</td><td>27</td><td>28</td></tr>
    </table>
    <div class="abs cal-btn" style="left:9px;width:50px">Today</div>
    <div class="abs cal-btn" style="left:126px;width:45px;color:var(--cal-blue)">Done</div>
  </div>

  <div class="abs side-head" style="top:755px">Custommer Service</div>
  <div class="abs service-photo" role="img" aria-label="Smiling customer service staff wearing headsets"></div>

  <div class="abs side-head light" style="top:948px">News Flash</div>
  <p class="abs news">Lorem ipsum dolor sit amet, consectetuer adipiscing elit, sed diam nonummy nibh euismod tincidunt ut laoreet dolore magna aliquam erat volutpat. Ut wisi enim</p>
  <div class="abs btn" style="left:140px;top:1087px;width:80px">More</div>
</aside>

<main class="abs main">
  <section class="abs card" style="left:4px">
    <div class="photo" role="img" aria-label="Divers preparing to enter clear blue water from a boat" style="background:linear-gradient(#cfdbe2,#6fa9c6 45%,#1f8fb4)"></div>
    <h3>Diving</h3>
    <p>Lorem ipsum dolor sit amet, consectetuer adipiscing elit, sed diam nonummy nibh euismod tincidunt ut laoreet dolore magna aliquam erat volutpat. Ut wisi enim</p>
    <div class="btn" style="left:118px">More</div>
  </section>
  <section class="abs card" style="left:220px">
    <div class="photo" role="img" aria-label="Seafood served in a coconut with fresh papaya" style="background:linear-gradient(135deg,#5a2412,#b8622c 50%,#e0923a)"></div>
    <h3>Restaurant</h3>
    <p>Lorem ipsum dolor sit amet, consectetuer adipiscing elit, sed diam nonummy nibh euismod tincidunt ut laoreet dolore magna aliquam erat volutpat. Ut wisi enim</p>
    <div class="btn" style="left:114px">More</div>
  </section>
  <section class="abs card" style="left:435px">
    <div class="photo" role="img" aria-label="Guest meditating on a lounger in a tropical garden" style="background:linear-gradient(#8db07a,#c7d1c0 55%,#5c5a55)"></div>
    <h3>Relaxation</h3>
    <p style="top:173px">Lorem ipsum dolor sit amet, consectetuer adipiscing elit, sed diam nonummy nibh euismod tincidunt ut laoreet dolore magna aliquam erat volutpat. Ut wisi enim</p>
    <div class="btn" style="left:116px">More</div>
  </section>

  <h2>Lorem Ipsum</h2>
  <hr>
  <div class="body">
    <p>Lorem ipsum dolor sit amet, consectetuer adipiscing elit, sed diam nonummy nibheuismod tincidunt ut laoreet dolore magna aliquam erat volutpat. Ut wisi enim</p>
    <p>Lorem ipsum dolor sit amet, consectetuer adipiscing elit, sed diam nonummy nibheuismod tincidunt ut laoreet dolore magna aliquam erat volutpat. Ut wisi enim</p>
    <p>Lorem ipsum dolor sit amet, consectetuer adipiscing elit, sed diam nonummy nibheuismod tincidunt ut laoreet dolore magna aliquam erat volutpat. Ut wisi enim</p>
    <p>Lorem ipsum dolor sit amet, consectetuer adipiscing elit, sed diam nonummy nibheuismod tincidunt ut laoreet dolore magna aliquam erat volutpat. Ut wisi enim</p>
    <p>Lorem ipsum dolor sit amet, consectetuer adipiscing elit, sed diam nonummy nibheuismod tincidunt ut laoreet dolore magna aliquam erat volutpat. Ut wisi enim</p>
    <p>Lorem ipsum dolor sit amet, consectetuer adipiscing elit, sed diam nonummy nibheuismod tincidunt ut laoreet dolore magna aliquam erat volutpat. Ut wisi enim</p>
  </div>
</main>

<footer>
  <div class="abs rule-thick"></div>
  <div class="abs rule-thin"></div>
  <div class="abs footer-name">Kerrow Vale</div>
  <div class="abs footer-line" style="top:1167px">Your address Here</div>
  <div class="abs footer-line" style="top:1182px">Your phone/contact Here</div>
  <div class="abs copyright">Copyright 2014</div>
</footer>

</body>
</html>
```